Eyecatching website design for commercial lighting business

This contest is all about the graphic design aspect. We need a striking website design for a commercial lighting company. We want something really eye catching to introduce people to our range of induction and LED lights which save businesses money on maintenance and electricity costs.

To be successful in this contest you will need to provide a design and pictures for the pages listed below.

We are using the platform talvo.com.au and you can see the attached template which everything will be loaded into so we just need HTML files which we can upload and we can do everything else from Talvo.

The final design should be strong and clean and use the colours and textures in the attached business card file.

Detailed requirements:

Please see attached screenshot of the website template, all we need is a fantastic graphic design and improvement/ incorporation of our logo for the following pages
Page Headings:
1. Home
About Us, Contact Us, snapshot of and link to Blog

Each of the below pages will have several paragraphs of text followed by a list of suitable products which is generated from our product catalogue.

2. Car Park Lighting
3. Educational Lighting
4. Hospitality Lighting
5. Office & Shop Lighting
6. Warehouse Lighting

Some of the website we have seen which are similar in nature are:
http://www.quorbenlamps.com.au/
http://www.yimra.com/
http://www.brightvane.net/commercial-led
but we really want a modern, eye catching and memorable design

Some of the designs built on Talvo that we like are:

http://www.harbourmarket.com.au/
http://www.tacklebay.com.au/
http://www.wenbrook.com.au/

I've also uploaded a couple of photos that we love. We'd like something similar for each industry.

Target Market(s)

Company Owners, Maintenance & Facilities Managers, Electrical Contractors

Industry/Entity Type

Electrical

Coding

Coded - Design and coding required

Number of Pages Required

5+ page

Font styles to use
Sans Serif

Colors
33a6d7
ec1f27

Requirements
Must have
• -Must scale to mobile
• -HTML coded files need to be provided (HTML Bootstrap)
Nice to have
• -Prefer incorporation of our logo into header bar
• -Design of 2-3 advertising banners which can be displayed on the home page
• -Prominent call to action button towards top of page 'Get a quote' or similar
• -Grid based design HTML Bootstrap

```html
<!DOCTYPE html>
<html lang="en">
<head>
<meta charset="utf-8">
<title>K&amp;R Avery Business Solutions – Commercial Lighting</title>
<link href="https://fonts.googleapis.com/css2?family=Open+Sans:wght@400;600;700&family=Oswald:wght@400;500&display=swap" rel="stylesheet">
<style>
:root{
  --red:#d3262c;
  --red-dark:#8e1418;
  --blue:#33a6d7;
  --blue-deep:#1f6fb0;
  --navy:#1b3f7a;
  --navy-dark:#142f5c;
  --grey:#f1f1f1;
  --text:#555;
  --white:#fff;
}
*{box-sizing:border-box;margin:0;padding:0}
html,body{width:788px;height:1200px;overflow:hidden}
body{font-family:"Open Sans",sans-serif;color:var(--text);background:var(--white);font-size:9px;line-height:1.45}
.site-header{height:82px;background:linear-gradient(135deg,#6e0f12 0%,var(--red) 45%,#7a1014 100%);position:relative}
.brand{position:absolute;left:48px;top:14px;display:flex;align-items:center;gap:8px;color:var(--white);font-weight:700;font-size:17px;letter-spacing:.5px}
.brand-mark{width:22px;height:22px;border-radius:50%;background:var(--white)}
.brand small{display:block;font-size:9px;font-weight:600;letter-spacing:1.5px}
.header-tools{position:absolute;right:46px;top:26px;display:flex;gap:10px;align-items:center}
.search{width:110px;height:18px;background:var(--white);border-radius:2px;font-size:8px;color:#999;padding:3px 6px}
.cart{height:18px;background:var(--white);border-radius:2px;font-size:8px;color:#666;padding:3px 6px;width:70px}
.account{color:var(--white);font-size:8px}
.main-nav{height:26px;border-bottom:1px solid #ddd;display:flex;padding-left:47px}
.main-nav a{display:block;padding:0 11px;line-height:26px;color:var(--blue-deep);text-decoration:none;font-size:9px;font-weight:600}
.main-nav a.active{background:var(--blue-deep);color:var(--white)}
.layout{display:flex;gap:24px;padding:22px 46px 0 47px;height:622px}
.sidebar{width:128px;flex:none}
.side-box{margin-bottom:14px}
.side-title{color:var(--white);font-size:11px;padding:5px 7px;background:var(--red)}
.side-title.blue{background:var(--blue-deep)}
.side-list{list-style:none;border:1px solid #ddd;border-top:0}
.side-list li{padding:5px 8px;color:var(--blue);border-top:1px solid #eee;font-size:9px}
.history{border:1px solid #ddd;border-top:0;padding:8px;display:flex;gap:6px;height:92px}
.history-thumb{width:34px;height:34px;background:linear-gradient(#666,#ccc);flex:none}
.history p{font-size:8px;color:var(--red);line-height:1.3}
.history .price{color:#333;margin-top:4px}
.history .price s{color:#999}
.side-ad{height:112px;background:linear-gradient(160deg,#c6e4f4,#ffffff 55%,#e34a4f);margin-top:28px}
.content{flex:1}
.hero{height:210px;background:radial-gradient(ellipse at 50% 40%,#e8ecef,#8e959a 60%,#4b5156);border:1px solid #ccc}
.welcome{font-family:"Oswald",sans-serif;color:var(--red);font-size:24px;font-weight:500;margin-top:12px;line-height:1.1}
.tagline{color:var(--blue-deep);font-size:12px;margin-bottom:8px}
.content p{margin-bottom:8px;font-size:8.5px}
.process{color:var(--red);font-size:12px;font-weight:600;margin:6px 0 6px}
.benefits{list-style:none}
.benefits li{background:var(--blue-deep);color:var(--white);font-size:9.5px;padding:3px 8px 3px 22px;margin-bottom:3px;position:relative}
.benefits svg{position:absolute;left:7px;top:5px}
.cta-band{height:250px;background:radial-gradient(ellipse at 50% 60%,#e2353b,var(--red-dark) 80%);color:var(--white);text-align:center;padding-top:46px}
.cta-band p{font-size:12px;line-height:1.6}
.call{display:flex;justify-content:center;align-items:center;gap:14px;margin-top:20px;font-size:17px}
.call-icon{width:34px;height:34px;border-radius:50%;border:2px solid var(--white);display:flex;align-items:center;justify-content:center}
.call strong{font-size:19px;font-weight:600}
.site-footer{height:195px;background:linear-gradient(var(--navy),var(--navy-dark));display:flex;padding:22px 46px 0 47px;gap:20px}
.footer-col{flex:1;color:#c9d6ea}
.footer-col h3{color:var(--white);font-size:13px;font-weight:400;margin-bottom:8px}
.footer-col ul{list-style:none}
.footer-col li{font-size:8.5px;margin-bottom:2px}
.footer-col li.hot{color:#f05a5f}
.footer-col p{font-size:8px}
.socials{display:flex;gap:8px;margin-top:8px}
.socials span{width:10px;height:10px;border-radius:50%;background:var(--red)}
.copyright{height:31px;background:#e9ecf2;text-align:center;line-height:31px;font-size:8px;color:#777}
.copyright b{color:var(--red);font-weight:600}
</style>
</head>
<body>
<header class="site-header">
  <div class="brand"><span class="brand-mark"></span><div>K&amp;R Avery<small>BUSINESS SOLUTIONS</small></div></div>
  <div class="header-tools">
    <div class="search">Search here...</div>
    <div class="cart">Empty Cart</div>
    <div class="account">My Account</div>
  </div>
</header>
<nav class="main-nav">
  <a class="active">Home</a><a>Car parking</a><a>Educational lighting</a><a>Office &amp; Shop lighting</a><a>Warehouse lighting</a><a>All products</a><a>Blog</a>
</nav>
<div class="layout">
  <aside class="sidebar">
    <div class="side-box">
      <div class="side-title">Categories</div>
      <ul class="side-list"><li>› Induction Lighting</li></ul>
    </div>
    <div class="side-box" style="margin-top:40px">
      <div class="side-title blue">Browse History</div>
      <div class="history">
        <div class="history-thumb" role="img" aria-label="High bay light fitting"></div>
        <div><p>230w Weatherproof High Bay - Natural Light</p><p class="price">$468.40 <s>$536</s></p></div>
      </div>
    </div>
    <div class="side-box" style="margin-top:34px">
      <div class="side-title">Information</div>
      <ul class="side-list"><li>› About us</li><li>› Return policy</li><li>› Contact us</li></ul>
    </div>
    <div class="side-ad" role="img" aria-label="Advertising banner for a ski chalet holiday"></div>
  </aside>
  <main class="content">
    <div class="hero" role="img" aria-label="Brightly lit underground car park tunnel"></div>
    <h1 class="welcome">WELCOME TO</h1>
    <div class="tagline">the Commercial Lighting Division of K&amp;R Avery Business Solutions</div>
    <p>Retrofitting the lighting in a commercial or industrial premises is a great way to save money on energy costs and maintenance, create a safer work environment and reduce the load on the wiring in the premises.</p>
    <p>When you are considering a retrofit of a commercial building there are a number of technologies on the market and a lot to consider.</p>
    <div class="process">We make it an easy process by providing you with:</div>
    <ul class="benefits">
      <li><svg width="8" height="8" viewBox="0 0 8 8"><path d="M1 4l2 2 4-5" stroke="#fff" fill="none" stroke-width="1.5"/></svg>The best range of energy saving commercial &amp; industrial lighting</li>
      <li><svg width="8" height="8" viewBox="0 0 8 8"><path d="M1 4l2 2 4-5" stroke="#fff" fill="none" stroke-width="1.5"/></svg>High quality products from reputable manufacturers which meet Australian Standards</li>
      <li><svg width="8" height="8" viewBox="0 0 8 8"><path d="M1 4l2 2 4-5" stroke="#fff" fill="none" stroke-width="1.5"/></svg>Assistance to ensure you choose the right product for the right application</li>
    </ul>
    <p style="margin-top:8px">Situated in Glenfield the Commercial Lighting Division of K&amp;R Avery Business Solutions offers easy solutions for commercial retrofit of lighting throughout Victoria and we can also ship interstate.</p>
  </main>
</div>
<section class="cta-band">
  <p>With a highly experienced team and a strong range of quality products our staff are<br>available Monday to Friday 9am-5pm AEST to take Calls on</p>
  <div class="call">Take Calls on
    <span class="call-icon"><svg width="16" height="16" viewBox="0 0 24 24"><path fill="#fff" d="M6.6 10.8a15 15 0 006.6 6.6l2.2-2.2c.3-.3.7-.4 1-.2 1.1.4 2.3.6 3.6.6.6 0 1 .4 1 1V20c0 .6-.4 1-1 1A17 17 0 013 4c0-.6.4-1 1-1h3.5c.6 0 1 .4 1 1 0 1.3.2 2.5.6 3.6.1.3 0 .7-.2 1z"/></svg></span>
    <strong>(03) 9481 3027</strong></div>
</section>
<footer class="site-footer">
  <div class="footer-col"><h3>Services</h3><ul><li class="hot">› Car Parking</li><li>› Educational Lighting</li><li>› Hospitality Lighting</li><li>› Office &amp; Shop Lighting</li><li>› Warehouse Lighting</li></ul></div>
  <div class="footer-col"><h3>About Us</h3><p>Retrofitting the lighting in a commercial or industrial premises is a great way to save money on energy costs and maintenance, creates a safer work environment and reduces the load on the wiring in the premises.</p></div>
  <div class="footer-col"><h3>Information</h3><ul><li>› About us</li><li>› Return policy</li><li>› Contact us</li></ul></div>
  <div class="footer-col"><h3>Stay In Touch</h3><p>Talk to our lighting team about your next retrofit project today.</p><p>(03) 9481 3027</p><p>hello@kravery.com.au</p><div class="socials"><span></span><span></span></div></div>
</footer>
<div class="copyright">© <b>K&amp;R Avery Business Solutions</b> 2015. All Rights Reserved</div>
</body>
</html>
```